Mental Health care Company in Washington DC

We are a new mental health care services provider in Washington DC. Please look at these sites.
https://marlowbrookpartners.com
https://www.quillstoneinc.com
https://velmarsh-kt.org/
https://www.trivanqx.com
https://www.thelanternofqz.com

```html
<!DOCTYPE html>
<html lang="en">
<head>
<meta charset="utf-8">
<title>Novalen Health Services — Mental Health Care in Washington DC</title>
<link href="https://fonts.googleapis.com/css2?family=Plus+Jakarta+Sans:wght@400;500;600;700&family=Inter:wght@400;500;600&display=swap" rel="stylesheet">
<style>
:root{
  --blue:#0b5ff0;
  --blue-dark:#0846c4;
  --orange:#f5801f;
  --ink:#111318;
  --text:#1e2128;
  --muted:#6b6f78;
  --hero-bg:#f4f4f4;
  --navy:#0f1d3a;
  --line:#dcdde2;
  --white:#ffffff;
}
*{box-sizing:border-box;margin:0;padding:0}
html,body{width:1200px;height:2919px;overflow:hidden}
body{position:relative;font-family:"Plus Jakarta Sans",sans-serif;color:var(--text);background:linear-gradient(180deg,#f1eff1 560px,#f6f6f8 1400px,#eef0f4 2000px,#f3f4f7 2350px)}
.abs{position:absolute}
a{color:inherit;text-decoration:none}

/* header */
.hero-band{left:0;top:0;width:1200px;height:558px;background:var(--hero-bg)}
.brand{left:76px;top:24px;display:flex;flex-direction:column;align-items:center}
.brand-name{font-size:28px;font-weight:600;color:#1a2a52;letter-spacing:-.6px;line-height:1;white-space:nowrap}
.brand-sub{font-size:10px;letter-spacing:7px;color:#8c93a3;margin-top:4px}
.nav{left:322px;top:30px}
.nav a{position:absolute;font-size:20px;font-weight:500;color:var(--ink);white-space:nowrap}
.btn{display:flex;align-items:center;justify-content:center;border-radius:5px;font-weight:400}
.btn-primary{background:var(--blue);color:#fff;box-shadow:0 12px 22px rgba(11,95,240,.28)}
.btn-outline{border:2px solid var(--blue);color:var(--ink);background:#fff}
.book{left:963px;top:23px;width:160px;height:38px;font-size:13px;box-shadow:none}

.hero-title{left:76px;top:178px;font-size:42px;font-weight:700;line-height:49px;color:var(--ink);letter-spacing:-.5px}
.hero-sub{left:76px;top:340px;font-size:26px;color:var(--ink)}
.hero-cta1{left:76px;top:410px;width:177px;height:56px;font-size:20px}
.hero-cta2{left:275px;top:410px;width:178px;height:56px;font-size:20px}
.photo{background:linear-gradient(160deg,#e8c9d6 0%,#c9a7b4 35%,#7f8a5a 70%,#6b7a3e 100%)}
.hero-photo{left:645px;top:84px;width:555px;height:474px}

/* about */
.about-photo{left:80px;top:619px;width:427px;height:312px;border-radius:14px;background:linear-gradient(135deg,#2d3f63 0%,#e9e6e6 45%,#d4a99b 55%,#2a3a5e 100%)}
.about-title{left:608px;top:638px;font-size:26px;font-weight:700;color:var(--ink)}
.about-text{left:608px;top:690px;width:525px;font-size:18px;letter-spacing:-.3px;line-height:24.6px;color:var(--ink)}
.about-cta{left:608px;top:860px;width:176px;height:54px;font-size:20px}

/* services */
.section-title{left:0;width:1200px;text-align:center;font-size:27px;font-weight:700;color:var(--ink)}
.card{top:1071px;width:339px;height:557px;background:#fff;border-radius:8px;overflow:hidden;box-shadow:0 10px 40px rgba(120,150,230,.2)}
.card-photo{height:241px;width:100%}
.card-body{position:relative;padding:36px 27px 0}
.card-title{font-size:21px;font-weight:700;margin-bottom:28px}
.card-text{font-size:16.5px;letter-spacing:-.2px;line-height:20.6px;color:var(--ink);height:150px}
.card-foot{position:absolute;left:19px;right:19px;top:272px;border-top:1px solid var(--line);padding:14px 8px 0;display:flex;align-items:center;gap:13px;font-size:17px;color:var(--ink)}
.arrow-dot{width:29px;height:29px;border-radius:50%;display:flex;align-items:center;justify-content:center}
.blue .card-title{color:var(--blue)}
.blue .arrow-dot{background:var(--blue)}
.orange .card-title{color:var(--orange)}
.orange .arrow-dot{background:var(--orange)}

/* testimonials */
.quote{top:1755px;width:333px;height:253px;background:#fff;padding:30px 23px 0;font-family:"Inter",sans-serif;box-shadow:0 14px 30px rgba(120,150,230,.15)}
.quote-head{display:flex;justify-content:space-between;align-items:center}
.stars{font-size:18px;letter-spacing:1px}
.tag{display:flex;align-items:center;gap:4px;font-size:10px;font-weight:600;color:var(--ink)}
.tag i{width:12px;height:12px;border-radius:50%;display:block}
.quote p{font-size:14.5px;line-height:22px;color:var(--ink);margin-top:14px;height:132px}
.q-blue .stars{color:var(--blue)} .q-blue .tag i{background:#4263eb}
.q-orange .stars{color:var(--orange)} .q-orange .tag i{background:var(--orange)}
.q-orange p{line-height:19px;margin-top:22px}
.author{display:flex;align-items:center;gap:5px}
.avatar{width:33px;height:33px;border-radius:50%;background:linear-gradient(135deg,#b9a7c7,#5d5a78)}
.author b{display:block;font-size:12.5px;font-weight:600;color:var(--ink)}
.author small{display:block;font-size:9px;color:var(--muted)}
.pager{top:2062px;width:50px;height:50px;border:1.5px solid #2c3a6b;border-radius:50%;display:flex;align-items:center;justify-content:center}

/* contact */
.navy-band{left:0;top:2354px;width:1200px;height:565px;background:var(--navy)}
.contact-card{left:76px;top:2238px;width:1047px;height:382px;background:var(--blue);border-radius:18px}
.contact-title{left:125px;top:2308px;font-size:28px;font-weight:700;color:#fff}
.contact-text{left:125px;top:2367px;width:390px;font-size:13.5px;line-height:18.5px;color:#fff}
.contact-list{left:125px;top:2453px;list-style:none;color:#fff;font-size:12.5px}
.contact-list li{height:25px;display:flex;align-items:center;gap:8px}
.contact-list li::before{content:"";width:4px;height:4px;border-radius:50%;background:#fff}
.map{left:565px;top:2156px;width:513px;height:402px;border-radius:14px;background:linear-gradient(135deg,#d7e6d4 0%,#e6ecef 50%,#cfe0d0 100%)}

/* footer */
.f-brand{left:158px;top:2672px;width:170px;display:flex;flex-direction:column;align-items:center}
.f-brand .brand-name{color:#fff;font-size:24px}
.f-brand .brand-sub{color:#fff;letter-spacing:6px}
.socials{left:165px;top:2752px;display:flex;gap:28px}
.socials span{width:17px;height:17px;border-radius:50%;background:#fff;display:block}
.f-col{top:2676px;color:#fff;font-size:12.5px}
.f-col h4{font-size:15px;font-weight:500;margin-bottom:24px}
.f-col a{display:block;margin-bottom:27px}
.newsletter{left:783px;top:2664px;width:252px;height:159px;background:var(--blue-dark);border-radius:4px;padding:15px 12px;color:#fff}
.newsletter h4{font-size:15px;font-weight:600}
.sub-form{display:flex;margin-top:24px;height:34px}
.sub-form input{flex:1;min-width:0;border:0;font:9px "Plus Jakarta Sans",sans-serif;padding:0 8px;color:var(--muted);background:#fff;border-radius:2px 0 0 2px}
.sub-form button{width:88px;border:0;background:var(--blue);color:#fff;font:600 10.5px "Plus Jakarta Sans",sans-serif;border-radius:0 2px 2px 0}
.newsletter small{display:block;margin-top:15px;font-size:9.5px;line-height:14px;color:#c9d6ff}
.f-line{left:68px;top:2879px;width:1064px;height:1px;background:#7b8398}
.copy{left:0;top:2891px;width:1200px;text-align:center;color:#fff;font-size:13.5px}
</style>
</head>
<body>

<div class="abs hero-band"></div>

<div class="abs brand"><span class="brand-name">Novalen Health</span><span class="brand-sub">SERVICES</span></div>

<nav class="abs nav">
  <a href="#" style="left:0">Home</a>
  <a href="#" style="left:99px">About</a>
  <a href="#" style="left:200px">Services</a>
  <a href="#" style="left:322px">Testimonials</a>
  <a href="#" style="left:480px">Contact</a>
</nav>
<a href="#" class="abs btn btn-primary book">Book Consultation</a>

<h1 class="abs hero-title">Your Trusted Mental<br>Health Partner in<br>Washington DC</h1>
<p class="abs hero-sub">Personal care, professional, support</p>
<a href="#" class="abs btn btn-primary hero-cta1">Get Started</a>
<a href="#" class="abs btn btn-outline hero-cta2">Learn More</a>
<div class="abs photo hero-photo" role="img" aria-label="Photo of a family enjoying a picnic under cherry blossom trees in a park"></div>

<div class="abs about-photo" role="img" aria-label="Photo of a caregiver gently holding a client's hands"></div>
<h2 class="abs about-title">Who We Are</h2>
<p class="abs about-text">Novalen Health is a mental health service provider based in Washington, DC. We offer compassionate, personalized care for individuals, families, and communities seeking support. Our licensed professionals are dedicated to guiding clients through their healing journey in a safe, respectful, and confidential environment.</p>
<a href="#" class="abs btn btn-primary about-cta">Learn More</a>

<h2 class="abs section-title" style="top:992px">What Novalen Health</h2>

<article class="abs card blue" style="left:76px">
  <div class="card-photo" role="img" aria-label="Photo of a therapist in a one-on-one session with a client in a bright room" style="background:linear-gradient(135deg,#e9e3da,#c7b9a6 60%,#8a7b6a)"></div>
  <div class="card-body">
    <h3 class="card-title">Individual Therapy</h3>
    <p class="card-text">Personalized one-on-one sessions designed to help you explore your thoughts, emotions, and challenges in a safe, confidential space. Our therapists work with you to build coping strategies, self-awareness, and emotional resilience.</p>
    <div class="card-foot">Show Details <span class="arrow-dot"><svg width="14" height="14" viewBox="0 0 14 14"><path d="M2 7h10M8 3l4 4-4 4" stroke="#fff" stroke-width="2" fill="none" stroke-linecap="round" stroke-linejoin="round"/></svg></span></div>
  </div>
</article>

<article class="abs card orange" style="left:430px">
  <div class="card-photo" role="img" aria-label="Photo of a group counseling circle on bean bags" style="background:linear-gradient(135deg,#9fb08c,#8c8a98 55%,#5a5868)"></div>
  <div class="card-body">
    <h3 class="card-title">Group Counseling</h3>
    <p class="card-text">A supportive environment where individuals with similar challenges come together to share experiences, learn from one another, and grow. Guided by a licensed therapist, group sessions promote connection, empathy, and healing.</p>
    <div class="card-foot">Show Details <span class="arrow-dot"><svg width="14" height="14" viewBox="0 0 14 14"><path d="M2 7h10M8 3l4 4-4 4" stroke="#fff" stroke-width="2" fill="none" stroke-linecap="round" stroke-linejoin="round"/></svg></span></div>
  </div>
</article>

<article class="abs card blue" style="left:785px">
  <div class="card-photo" role="img" aria-label="Photo of a family with their child talking with a therapist on a sofa" style="background:linear-gradient(135deg,#6e6f72,#d9d6d2 55%,#a39a90)"></div>
  <div class="card-body">
    <h3 class="card-title">Family Therapy</h3>
    <p class="card-text">Focused sessions that address communication, conflict, and relationships within the family unit. Family therapy helps strengthen bonds, improve understanding, and foster a healthier, more supportive home environment.</p>
    <div class="card-foot">Show Details <span class="arrow-dot"><svg width="14" height="14" viewBox="0 0 14 14"><path d="M2 7h10M8 3l4 4-4 4" stroke="#fff" stroke-width="2" fill="none" stroke-linecap="round" stroke-linejoin="round"/></svg></span></div>
  </div>
</article>

<h2 class="abs section-title" style="top:1691px">What Our Clients Say</h2>

<div class="abs quote q-blue" style="left:76px">
  <div class="quote-head"><span class="stars">★★★★★</span><span class="tag"><i></i>Testimonial</span></div>
  <p>Dude, your support is the bomb! Mental health is the real deal! I STRONGLY recommend focusing on mental well-being to EVERYONE who wants to thrive in life and business!</p>
  <div class="author"><span class="avatar"></span><div><b>Mira Castellane</b><small>Senior Paradigm Strategist</small></div></div>
</div>
<div class="abs quote q-orange" style="left:433px">
  <div class="quote-head"><span class="stars">★★★★★</span><span class="tag"><i></i>Testimonial</span></div>
  <p>Your approach to mental health has truly changed the game for me. Prioritizing my mind has been the best decision, and I recommend it to anyone chasing real, lasting success.</p>
  <div class="author"><span class="avatar"></span><div><b>Mrs. Oderwald</b><small>Legacy Usability Manager</small></div></div>
</div>
<div class="abs quote q-blue" style="left:791px">
  <div class="quote-head"><span class="stars">★★★★★</span><span class="tag"><i></i>Testimonial</span></div>
  <p style="margin-top:22px">Mental health isn’t optional — it’s essential. I never realized how powerful it is until I focused on it. Total game-changer!</p>
  <div class="author"><span class="avatar"></span><div><b>Tobin Raskell</b><small>District Assurance Officer</small></div></div>
</div>

<a href="#" class="abs pager" style="left:527px" aria-label="Previous"><svg width="16" height="22" viewBox="0 0 16 22"><path d="M12 2 3 11l9 9" stroke="#1b2550" stroke-width="2.2" fill="none" stroke-linecap="round" stroke-linejoin="round"/></svg></a>
<a href="#" class="abs pager" style="left:624px" aria-label="Next"><svg width="16" height="22" viewBox="0 0 16 22"><path d="M4 2l9 9-9 9" stroke="#1b2550" stroke-width="2.2" fill="none" stroke-linecap="round" stroke-linejoin="round"/></svg></a>

<div class="abs navy-band"></div>
<div class="abs contact-card"></div>
<h2 class="abs contact-title">Visit Us or Reach Out</h2>
<p class="abs contact-text">Whether you’re ready to begin your mental health journey or just have a few questions, we’re here for you. Feel free to visit our office or contact us through phone, email, or the form below — we’d love to hear from you.</p>
<ul class="abs contact-list">
  <li>Tel.: +1 202 555 0143</li>
  <li>Mobil: +1 202 555 0178</li>
  <li>Fax: +1 202 555 0192</li>
  <li>hello@novalenhealth.example</li>
</ul>
<div class="abs map" role="img" aria-label="Map of the Washington DC area showing the office location"></div>

<div class="abs f-brand"><span class="brand-name">Novalen Health</span><span class="brand-sub">SERVICES</span></div>
<div class="abs socials" aria-label="Social links"><span></span><span></span><span></span><span></span></div>

<div class="abs f-col" style="left:385px"><h4>Company</h4><a href="#" style="font-weight:600">About</a></div>
<div class="abs f-col" style="left:502px"><h4>Legal</h4><a href="#">Privacy Policy</a><a href="#">Terms &amp; Services</a><a href="#">Terms of Use</a><a href="#">Refund Policy</a></div>
<div class="abs f-col" style="left:642px;top:2674px"><h4>Quick Links</h4><a href="#">Home</a><a href="#" style="margin-top:-2px">Services</a><a href="#" style="margin-top:-8px">Contact</a></div>

<div class="abs newsletter">
  <h4>Join Our Newsletter</h4>
  <div class="sub-form"><input type="email" placeholder="Your email address"><button>Subscribe</button></div>
  <small>* Will send you weekly updates for your better tool management.</small>
</div>

<div class="abs f-line"></div>
<p class="abs copy">novalen health- All Rights Reserved. Copyright © 2025</p>

</body>
</html>
```